Chemical Blender Web Design Project

We are a chemical blender for wholesale and retail. The website is for info only, not for e-commerce.
We blend safer high performance corrosion and scale inhibitors. FYI - These products are used in a variety of equipment and piping. Corrosion inhibitors help prevent metal from corroding which helps equipment and piping last longer. Scale inhibitors help prevent scale from forming on equipment and piping which provides better heat transfer and saves energy costs.
We also have 2 patents. One is for a water conservation process for cooling towers. The other is for remediation/environmental clean-up process that works in soil, water and sludge.
I would like blue and green (clean water) colors on the website. Our current website is vortalyn.com. Our logo can be found at vortalyn.com/logo.htm. It is an original drawing and is in the process of being registered. The water pictures are ones I took, you may use those for our site, if you would like.
Websites I like- http://www.brivex.com/, http://qmpureflow.com/index.html and http://tandorite.com/.
I would like to see who visited our website.
Thank you!

```html
<!DOCTYPE html>
<html lang="en">
<head>
<meta charset="utf-8">
<title>VORTALYN International, Inc.</title>
<link rel="stylesheet" href="https://fonts.googleapis.com/css2?family=Signika:wght@300;400&family=Ubuntu:wght@400&display=swap">
<style>
:root{
  --sky:#c9e2f7;
  --sky-deep:#9cc9ef;
  --nav:#1788dc;
  --nav-dark:#0c72c4;
  --brand:#1f5fa8;
  --link:#1e74c4;
  --copy:#2a78c8;
  --ink:#333;
  --line:#b9d4ee;
  --white:#fff;
}
*{margin:0;padding:0;box-sizing:border-box}
html,body{width:1102px;height:1200px;overflow:hidden}
body{background:linear-gradient(90deg,var(--sky-deep),var(--sky) 8%,#e8f3fc 50%,var(--sky) 92%,var(--sky-deep));font-family:"Ubuntu",sans-serif}
.stage{position:relative;width:1126px;height:1226px;transform:scale(.97869);transform-origin:0 0}
.page{position:absolute;left:43px;top:0;width:1035px;height:1133px;background:var(--white);border:1px solid var(--line);border-top:0}
.abs{position:absolute}
.header-art{left:380px;top:0;width:654px;height:147px;background:linear-gradient(90deg,#fff 0%,#e3f1fc 35%,#bfe0f8 60%,#d8ecfb 100%)}
.brand{left:120px;top:68px;color:var(--brand);font-size:27px;line-height:27px;display:flex;align-items:center;gap:12px}
.brand-dot{width:16px;height:16px;border-radius:50%;background:var(--brand)}
.search{left:755px;top:83px;width:252px;height:35px;display:flex;align-items:center}
.search-field{width:218px;height:35px;border:1px solid var(--line);border-right:0;background:var(--white);font-size:12px;color:#456;padding:11px 10px;border-radius:4px 0 0 4px}
.search-go{width:35px;height:35px;border-radius:50%;background:var(--nav-dark);color:var(--white);font-size:14px;display:flex;align-items:center;justify-content:center;margin-left:-1px}
.nav{left:0;top:147px;width:1035px;height:51px;background:linear-gradient(var(--nav),var(--nav-dark));display:flex;padding-left:16px}
.nav a{color:var(--white);text-decoration:none;font-family:"Signika",sans-serif;font-size:16px;line-height:51px;padding:0 24px;border-right:1px solid rgba(0,40,90,.35)}
.nav a:last-child{border-right:0}
.hero{left:4px;top:205px;width:1023px;height:292px;border-radius:6px;background:linear-gradient(100deg,#c6935a 0%,#a0673a 16%,#2a86c4 26%,#1b66b0 55%,#2b7fc6 72%,#3b8bd0 100%)}
.hero-panel{left:705px;top:211px;width:316px;height:279px;background:var(--white);border-radius:6px}
.hero-item{position:relative;height:88px;border-bottom:1px solid #c9dbee;padding:16px 0 0 104px}
.hero-item:last-child{border-bottom:0}
.thumb{position:absolute;border:2px solid #dfe9f4;border-radius:3px}
.hero-item .thumb{left:18px;top:16px;width:79px;height:65px}
.hero-item h3{font-family:"Signika",sans-serif;font-weight:300;font-size:18px;color:var(--link);line-height:24px}
.hero-item p{font-size:11.5px;line-height:17px;color:var(--copy)}
.section-title{font-family:"Signika",sans-serif;font-weight:300;font-size:21px;color:var(--brand)}
.welcome{left:20px;top:518px;width:660px}
.welcome p{font-size:11.2px;line-height:18px;color:var(--copy);margin-top:0}
.welcome .section-title{margin-bottom:7px}
.gap{height:18px}
.news-title{left:23px;top:783px}
.news{position:absolute;width:308px}
.news h4{font-family:"Signika",sans-serif;font-weight:400;font-size:13.5px;line-height:18px;color:var(--link)}
.news p{font-size:11.2px;line-height:18px;color:var(--ink);margin-top:8px}
.news .more{font-family:"Signika",sans-serif;font-size:15px;color:#222;margin-top:6px}
.vrule{left:345px;top:820px;height:272px;border-left:1px dotted #8fb6dc}
.hrule{left:25px;top:944px;width:660px;border-top:1px dotted #8fb6dc}
.side{left:704px;top:508px;width:317px;height:592px;border:1px solid #d3e5f5;border-radius:6px;background:linear-gradient(#f1f8fe,#fbfdff 70%,#fff)}
.side-title{left:18px;top:16px;font-family:"Signika",sans-serif;font-weight:300;font-size:20px;color:#1a2a3a}
.prod{position:absolute;left:14px;width:300px;height:110px}
.prod .thumb{left:0;top:0;width:104px;height:88px}
.prod h3{position:absolute;left:117px;top:0;font-family:"Signika",sans-serif;font-weight:300;font-size:16px;color:var(--link)}
.prod p{position:absolute;left:117px;top:22px;width:180px;font-size:11.2px;line-height:17px;color:var(--copy)}
.prod .more{display:block;color:var(--link)}
.view-more{left:10px;top:530px;width:298px;height:29px;border-radius:3px;background:linear-gradient(90deg,#eaf4fd,#d7eafa);text-align:right;padding:4px 18px 0 0;font-family:"Signika",sans-serif;font-size:15px;color:var(--link)}
.footer-text{left:64px;top:1149px;font-size:11.5px;color:#2a5c90}
.social{left:963px;top:1150px;display:flex;gap:4px}
.social span{width:20px;height:20px;border-radius:3px;background:#5d9ee0}
</style>
</head>
<body>
<div class="stage">
  <div class="page">
    <div class="abs header-art" role="img" aria-label="Splash of clear blue water"></div>
    <div class="abs brand"><span class="brand-dot"></span><span>VORTALYN<br>International, Inc.</span></div>
    <div class="abs search"><div class="search-field">Enter keyword..</div><div class="search-go">Go</div></div>
    <nav class="abs nav"><a>Home</a><a>About Us</a><a>Products</a><a>Equipment</a><a>Services</a><a>Contact Us</a></nav>

    <div class="abs hero" role="img" aria-label="Rocky coastline beside a deep blue sea"></div>
    <div class="abs hero-panel">
      <div class="hero-item"><div class="thumb" role="img" aria-label="Red controller pump" style="background:linear-gradient(135deg,#ddd,#b33 60%,#555)"></div><h3>Controllers Pumps</h3><p>Brightmesh Studio is a professional<br>website design company</p></div>
      <div class="hero-item"><div class="thumb" role="img" aria-label="Industrial boiler machine" style="background:linear-gradient(135deg,#eee,#8a8a8a 60%,#555)"></div><h3>Boilers</h3><p>Brightmesh Studio is a professional<br>website design company</p></div>
      <div class="hero-item"><div class="thumb" role="img" aria-label="Blue potable water tank" style="background:linear-gradient(135deg,#cde,#1f6fe0 55%,#345)"></div><h3>Potable Water</h3><p>Brightmesh Studio is a professional<br>website design company</p></div>
    </div>

    <section class="abs welcome">
      <h1 class="section-title">Welcome to Our Website Mainpage</h1>
      <p>Brightmesh Studio is a web service company, offering a wide range of services which range from designing and development, that is covering almost all the fields in the best possible way. To be the best we know what and how to present beautifully the working of the client’s need and their advantages be highlighted. We act in accordance with the Industry certified processes to deliver the best to our clients all over the world.</p>
      <div class="gap"></div>
      <p>Thus, Wanna get ahead in the competition with other websites…. Brightmesh Studio provide you with an attractive and most convincing website to enhance your marketing goals.<br>The only way to success is through the right path and that’s what we provide you. None of the other companies has the result we do. So stick to the best that’s how you will be the best don’t opt for the second best. Our expertise does not limit itself to web development but also it includes Web Hosting, Search Engine Optimization, E-Commerce. We partner hundreds of organization to enhance their business, marketing and profit goals.</p>
    </section>

    <h2 class="abs section-title news-title">Recent News &amp; Events</h2>
    <div class="abs vrule"></div>
    <div class="abs hrule"></div>
    <article class="news" style="left:25px;top:824px"><h4>2012 Water Technology Company of the Year by Aqua Market Review Readership</h4><p>Brightmesh Studio is a professional website design company dedicated to provide excellent services.</p><div class="more">read more »</div></article>
    <article class="news" style="left:361px;top:824px"><h4>Announces Water and Process Services Price Increase</h4><p>Brightmesh Studio is a professional website design company dedicated to provide excellent services.</p><div class="more">read more »</div></article>
    <article class="news" style="left:27px;top:965px"><h4>Lumaris Announces Commitment to Earth Habitat Fund and the Coalition for River Care</h4><p>Brightmesh Studio is a professional website design company dedicated to provide excellent services.</p><div class="more">read more »</div></article>
    <article class="news" style="left:364px;top:965px"><h4>Receives Three 2012 Manufacturing Industry Leaders 100 Awards</h4><p>Brightmesh Studio is a professional website design company dedicated to provide excellent services.</p><div class="more">read more »</div></article>

    <aside class="abs side">
      <h2 class="abs side-title">Our Chemical &amp; Eqipments</h2>
      <div class="prod" style="top:58px"><div class="thumb" role="img" aria-label="Glass beakers of blue chemical" style="background:linear-gradient(135deg,#e6eef2,#6fc2e8 60%,#2a9fd8)"></div><h3>Chemical products</h3><p>We here modify the site to improve the ranking by using the keywords and contents.<span class="more">read more »</span></p></div>
      <div class="prod" style="top:171px"><div class="thumb" role="img" aria-label="Row of controller valves" style="background:linear-gradient(135deg,#dbe8f4,#4e7fb8 55%,#1a2a3a)"></div><h3>Controllers Valves</h3><p>We here modify the site to improve the ranking by using the keywords and contents.<span class="more">read more »</span></p></div>
      <div class="prod" style="top:288px"><div class="thumb" role="img" aria-label="Stainless closed loop tank" style="background:linear-gradient(135deg,#cfd6dc,#8b949c 55%,#4a5058)"></div><h3>Closed Loops</h3><p>We here modify the site to improve the ranking by using the keywords and contents.<span class="more">read more »</span></p></div>
      <div class="prod" style="top:407px"><div class="thumb" role="img" aria-label="Water treatment basins from above" style="background:linear-gradient(135deg,#9db8a8,#5fa8a8 55%,#3f6c66)"></div><h3>Water Treatment Bases</h3><p>We here modify the site to improve the ranking by using the keywords and contents.<span class="more">read more »</span></p></div>
      <div class="abs view-more">view more »</div>
    </aside>
  </div>

  <p class="abs footer-text">Copyright © 2012 - 2012 VORTALYN International, Inc. All rights reserve</p>
  <div class="abs social" aria-label="Social links"><span></span><span></span><span></span><span></span></div>
</div>
</body>
</html>
```